Corvane Electrical Solutions

On one side. LOGO (underneath:) Commercial Industrial Residential

- NAME & CONTACT DETAILS

Marcus T. Hollings
Project Manager

(Cell icon) (441) 582-6197
(Email icon) cvnelectricalsoultions@mailventra.com
(Facebook & Instagram icons )@cvnelectricalsolutions

Other side: LOGO - underneath ELECTRICAL CONSTRUCTION & MAINTENANCE . LED LIGHTING & AUTOMATION . LIFE SAFETY SYSTEMS (FIRE ALARM / SECURITY) . DATA & COMMUNICATION

```html
<!DOCTYPE html>
<html lang="en">
<head>
<meta charset="utf-8">
<title>Corvane Electrical Solutions – Business Cards</title>
<link rel="stylesheet" href="https://fonts.googleapis.com/css2?family=Montserrat:wght@400;500;600;700&display=swap">
<style>
  :root {
    --page: #e6e7e9;
    --slate: #5a5b5d;
    --slate-ink: #2f3032;
    --slate-light: #d9dadc;
    --teal: #175d6e;
    --teal-deep: #114c5b;
    --paper: #ffffff;
    --ink: #3d4347;
    --accent: #1f6a7d;
  }
  * { box-sizing: border-box; margin: 0; padding: 0; }
  html, body { width: 1200px; height: 960px; overflow: hidden; }
  body {
    background: var(--page);
    font-family: "Montserrat", Arial, sans-serif;
    position: relative;
  }
  .card { position: absolute; box-shadow: 0 10px 24px rgba(0,0,0,.18); }

  /* Back of card: services */
  .card-services {
    left: 250px; top: 50px; width: 700px; height: 400px;
    background: var(--slate);
    padding: 0 70px;
    display: flex; flex-direction: column; justify-content: center;
  }
  .wordmark { display: flex; align-items: center; gap: 14px; }
  .wordmark-square { width: 22px; height: 22px; flex: none; }
  .wordmark-name { font-weight: 600; letter-spacing: .14em; text-transform: uppercase; }
  .card-services .wordmark-square { background: var(--slate-light); }
  .card-services .wordmark-name { color: var(--slate-light); font-size: 26px; }
  .services {
    margin-top: 48px; color: var(--slate-ink);
    font-size: 15px; font-weight: 500; line-height: 1.7;
  }
  .services span + span::before { content: " • "; }

  /* Front: contact panel */
  .card-contact {
    left: 250px; top: 500px; width: 345px; height: 400px;
    background: linear-gradient(135deg, var(--teal) 0%, var(--teal-deep) 100%);
    color: var(--paper);
    padding: 0 36px;
    display: flex; flex-direction: column; justify-content: center;
  }
  .person-name { font-size: 21px; font-weight: 700; letter-spacing: .03em; text-transform: uppercase; }
  .person-role { font-size: 14px; font-weight: 600; margin-top: 4px; }
  .contact-list { list-style: none; margin-top: 26px; font-size: 12.5px; }
  .contact-list li { display: flex; align-items: center; gap: 10px; margin-bottom: 7px; white-space: nowrap; }
  .contact-icon { width: 14px; height: 14px; flex: none; }

  /* Front: logo panel */
  .card-logo {
    left: 605px; top: 500px; width: 345px; height: 400px;
    background: var(--paper);
    padding: 0 30px;
    display: flex; flex-direction: column; justify-content: center;
  }
  .card-logo .wordmark { gap: 10px; }
  .card-logo .wordmark-square { background: var(--accent); width: 16px; height: 16px; }
  .card-logo .wordmark-name { color: var(--accent); font-size: 15px; }
  .sectors {
    margin-top: 16px; color: var(--ink);
    font-size: 11.5px; font-weight: 500; letter-spacing: .06em; text-transform: uppercase;
  }
  .sectors span + span::before { content: " • "; }
</style>
</head>
<body>

  <section class="card card-services">
    <div class="wordmark">
      <span class="wordmark-square"></span>
      <span class="wordmark-name">Corvane Electrical Solutions</span>
    </div>
    <p class="services">
      <span>Electrical Construction &amp; Maintenance</span><span>LED Lighting &amp; Automation</span><br>
      <span>Life Safety Systems (Fire Alarm / Security)</span><span>Data &amp; Communication</span>
    </p>
  </section>

  <section class="card card-contact">
    <h1 class="person-name">Marcus T. Hollings</h1>
    <p class="person-role">Project Manager</p>
    <ul class="contact-list">
      <li>
        <svg class="contact-icon" viewBox="0 0 14 14" aria-hidden="true">
          <rect x="3.5" y="1" width="7" height="12" rx="1.2" fill="none" stroke="currentColor" stroke-width="1.2"/>
          <line x1="6" y1="11" x2="8" y2="11" stroke="currentColor" stroke-width="1.2"/>
        </svg>
        (441) 582-6197
      </li>
      <li>
        <svg class="contact-icon" viewBox="0 0 14 14" aria-hidden="true">
          <rect x="1" y="3" width="12" height="8" fill="currentColor"/>
          <polyline points="1,3 7,8 13,3" fill="none" stroke="var(--teal)" stroke-width="1.2"/>
        </svg>
        cvnelectricalsoultions@mailventra.com
      </li>
      <li>
        <svg class="contact-icon" viewBox="0 0 14 14" aria-hidden="true"><circle cx="7" cy="7" r="6" fill="currentColor"/></svg>
        @cvnelectricalsolutions
      </li>
      <li>
        <svg class="contact-icon" viewBox="0 0 14 14" aria-hidden="true"><circle cx="7" cy="7" r="6" fill="currentColor"/></svg>
        @cvnelectricalsolutions
      </li>
    </ul>
  </section>

  <section class="card card-logo">
    <div class="wordmark">
      <span class="wordmark-square"></span>
      <span class="wordmark-name">Corvane Electrical Solutions</span>
    </div>
    <p class="sectors"><span>Commercial</span><span>Industrial</span><span>Residential</span></p>
  </section>

</body>
</html>
```